I would like some help creating my first business cards for my new business, I am a facilitator of a course that I have created. I am currently starting the sales promotion and marketing part of my business and need some help designing the business cards. Something fairly simple would be good, the core theme of my work is in connection of women to themselves and to each other. My initial design is a tree lit up by lights, a very mother earth type of image. This is not my design however so I probably am not legally able to use the design. I don't have a logo. Could you possibly assist with this?

I would really like to have the following details on the business card:
Mel Harbison
0431 582 904
hi.mel.harbison@quillpost.example

And also the image

Target Market(s)

Women who are living in an isolated environment

Industry/Entity Type

Counsellor

Contact Information for Business Card

Mel Harbison
Facilitator
hi.mel.harbison@quillpost.example
0431 582 904

Font styles to use
Other font styles liked:
• Handwriting - Dakota

Colors
e34197
fee18a
3276b5
33a6d7
33b8a4

Requirements
Must have
• 1) My details as above
• 2) a design (picture) that represents the mother earth theme similar to the designs included in the brief
• 3) no copyright attached to the design
• 4) Colours are very important but it is difficult to describe the colour using the colour wheel. Please refer to the example of the tree that I have included in the drop box.
• 5) I must apologise that I forgot to add the business card needs to have the name of the business in gold letters please: Riverstone Circle for Ladies, thank you
Nice to have
• It would be great to use the tree design that I included in the brief, this is my favourite picture but I think it is probably copyrighted. If it's not, that is the one I would like on my business cards please.

```html
<!DOCTYPE html>
<html lang="en">
<head>
<meta charset="utf-8">
<title>Mel Harbison – Business Card</title>
<link rel="stylesheet" href="https://fonts.googleapis.com/css2?family=Open+Sans:wght@400;600&display=swap">
<style>
  :root {
    --backdrop: #b3b3cf;
    --sky-blue: #33a6d7;
    --deep-blue: #3276b5;
    --rose-pink: #e34197;
    --butter-yellow: #fee18a;
    --gold: #f6c843;
    --mist-white: #f2f9fb;
    --ink: #111111;
  }
  * { margin: 0; padding: 0; box-sizing: border-box; }
  html, body {
    width: 1200px;
    height: 1200px;
    overflow: hidden;
    background: var(--backdrop);
    font-family: "Open Sans", Arial, sans-serif;
  }
  .business-card {
    position: absolute;
    left: 50px;
    top: 270px;
    width: 1100px;
    height: 660px;
    box-shadow: 0 8px 18px rgba(40, 40, 80, 0.25);
  }
  .card-shapes { position: absolute; inset: 0; }
  .identity {
    position: absolute;
    left: 750px;
    top: 145px;
    width: 300px;
    text-align: center;
  }
  .identity__name {
    font-size: 38px;
    font-weight: 400;
    color: var(--deep-blue);
    letter-spacing: -0.5px;
    line-height: 1.1;
    white-space: nowrap;
  }
  .identity__role {
    font-size: 26px;
    color: var(--rose-pink);
    line-height: 1.3;
  }
  .business-name {
    position: absolute;
    left: 36px;
    top: 612px;
    font-size: 26px;
    font-weight: 600;
    color: var(--gold);
    white-space: nowrap;
    line-height: 1.2;
  }
  .contact-row {
    position: absolute;
    display: flex;
    align-items: center;
    gap: 12px;
    color: var(--ink);
    white-space: nowrap;
  }
  .contact-row--phone { left: 690px; top: 360px; font-size: 34px; letter-spacing: 1px; }
  .contact-row--email { left: 604px; top: 428px; font-size: 22px; }
  .contact-icon { width: 44px; height: 44px; flex: none; }
</style>
</head>
<body>
  <div class="business-card">
    <svg class="card-shapes" width="1100" height="660" viewBox="0 0 1100 660">
      <defs>
        <radialGradient id="tree-glow" cx="50%" cy="55%" r="60%">
          <stop offset="0%" stop-color="#e8d9b0"/>
          <stop offset="30%" stop-color="#9b86b8"/>
          <stop offset="65%" stop-color="#2a2f6e"/>
          <stop offset="100%" stop-color="#141a45"/>
        </radialGradient>
        <linearGradient id="ground-tone" x1="0" y1="0" x2="0" y2="1">
          <stop offset="0%" stop-color="#1f7fa0" stop-opacity="0"/>
          <stop offset="100%" stop-color="#39b6a8" stop-opacity="0.85"/>
        </linearGradient>
        <clipPath id="artwork-clip"><circle cx="320" cy="290" r="248"/></clipPath>
      </defs>

      <rect class="field-yellow" width="1100" height="660" fill="var(--butter-yellow)"/>
      <polygon class="field-blue" points="0,0 620,0 750,330 410,660 0,660" fill="var(--sky-blue)"/>

      <g role="img" aria-label="Illustration of a glowing tree of light under a night sky, Mother Earth theme">
        <g clip-path="url(#artwork-clip)">
          <rect x="60" y="30" width="520" height="520" fill="url(#tree-glow)"/>
          <rect x="60" y="300" width="520" height="250" fill="url(#ground-tone)"/>
        </g>
      </g>

      <path class="arc-pink-inner" d="M520 30 A300 300 0 0 1 130 520" fill="none" stroke="var(--rose-pink)" stroke-width="24"/>
      <path class="arc-blue-inner" d="M580 90 A330 330 0 0 1 10 420" fill="none" stroke="var(--deep-blue)" stroke-width="22"/>
      <path class="arc-pink-outer" d="M590 430 A350 330 0 0 1 10 460" fill="none" stroke="var(--rose-pink)" stroke-width="26"/>

      <polygon class="panel-header" points="690,85 1060,85 1060,320 780,320" fill="var(--sky-blue)"/>
      <polygon class="panel-contact" points="780,320 1060,320 1060,600 500,600" fill="var(--mist-white)"/>
    </svg>

    <div class="identity">
      <h1 class="identity__name">MEL HARBISON</h1>
      <p class="identity__role">Facilitator</p>
    </div>

    <p class="business-name">Riverstone Circle for Ladies</p>

    <div class="contact-row contact-row--phone">
      <svg class="contact-icon" viewBox="0 0 44 44" aria-hidden="true">
        <circle cx="22" cy="22" r="22" fill="var(--deep-blue)"/>
        <path d="M15 11c1-1 3-1 4 1l2 4c.5 1 0 2-1 3l-1 1c1 3 3 5 6 6l1-1c1-1 2-1.5 3-1l4 2c2 1 2 3 1 4l-2 2c-2 2-7 1-12-4s-6-10-4-12z" fill="#fff"/>
      </svg>
      <span>0431 582 904</span>
    </div>

    <div class="contact-row contact-row--email">
      <svg class="contact-icon" viewBox="0 0 44 44" aria-hidden="true">
        <circle cx="22" cy="22" r="22" fill="var(--deep-blue)"/>
        <rect x="11" y="14" width="22" height="16" rx="1.5" fill="#fff"/>
        <path d="M11 15l11 9 11-9" fill="none" stroke="var(--deep-blue)" stroke-width="2"/>
      </svg>
      <span>hi.mel.harbison@quillpost.example</span>
    </div>
  </div>
</body>
</html>
```